Timber Ridge Land Services Business Cards

Need to create a business card with the company logo "Timber Ridge Land Services". The business will provide forestry mulching for land clearing and vegetation control, brush and small tree removal, wildlife habitat improvement and trail and property access creation.

```html
<!DOCTYPE html>
<html lang="en">
<head>
<meta charset="UTF-8">
<title>Timber Ridge Land Services – Business Cards</title>
<link rel="stylesheet" href="https://fonts.googleapis.com/css2?family=Rubik:wght@600;700&family=Poppins:wght@400;500&display=swap">
<style>
  :root {
    --stage: #252525;
    --forest: #025c46;
    --forest-deep: #0b6a4f;
    --teal: #0a9676;
    --leaf: #6abf69;
    --leaf-soft: #a4d795;
    --paper: #f2f4f3;
    --ink: #222;
    --ink-soft: #444;
    --silver-a: #d9d9d9;
    --silver-b: #ffffff;
  }
  html, body {
    margin: 0;
    padding: 0;
    width: 1200px;
    height: 1000px;
    overflow: hidden;
    background: var(--stage);
  }
  .card {
    position: absolute;
    left: 200px;
    width: 800px;
    height: 457px;
    border-radius: 28px;
    overflow: hidden;
  }
  .card-front { top: 30px; background: var(--forest); }
  .card-back  { top: 513px; background: var(--paper); }
  .wave { position: absolute; left: 0; top: 0; width: 800px; height: 457px; }

  .front-name {
    position: absolute;
    left: 0; right: 0; top: 190px;
    text-align: center;
    font-family: "Rubik", sans-serif;
    font-weight: 600;
    color: #fff;
    line-height: 1.15;
    font-size: 34px;
    letter-spacing: 0.5px;
  }
  .front-name span { display: block; font-size: 20px; letter-spacing: 1px; }

  .back-title {
    position: absolute;
    left: 33px; top: 30px;
    font-family: "Rubik", sans-serif;
    font-weight: 700;
    font-size: 29px;
    color: var(--forest-deep);
    margin: 0;
  }
  .back-subtitle {
    position: absolute;
    left: 33px; top: 68px;
    font-family: "Poppins", sans-serif;
    font-size: 20px;
    color: var(--ink-soft);
    margin: 0;
  }
  .website {
    position: absolute;
    right: 33px; top: 33px;
    font-family: "Poppins", sans-serif;
    font-size: 14px;
    letter-spacing: 1.6px;
    color: var(--ink-soft);
  }
  .website::before {
    content: "";
    display: inline-block;
    width: 11px; height: 3px;
    background: var(--leaf);
    vertical-align: middle;
    margin-right: 7px;
  }
  .contact {
    position: absolute;
    left: 33px; top: 124px;
    list-style: none;
    margin: 0; padding: 0;
    font-family: "Poppins", sans-serif;
    font-weight: 500;
    font-size: 18px;
    color: var(--ink);
  }
  .contact li { display: flex; align-items: flex-start; height: 32px; }
  .contact li.address { line-height: 29px; height: auto; }
  .contact svg { width: 22px; height: 22px; margin-right: 10px; margin-top: 4px; flex: none; fill: var(--forest-deep); }
  .back-name {
    position: absolute;
    left: 480px; width: 310px; top: 208px;
    text-align: center;
    font-family: "Rubik", sans-serif;
    font-weight: 700;
    color: var(--forest-deep);
    font-size: 31px;
    line-height: 1.1;
  }
  .back-name span { display: block; font-size: 18px; letter-spacing: 1px; }
</style>
</head>
<body>

<section class="card card-front">
  <svg class="wave" viewBox="0 0 800 457" aria-hidden="true">
    <defs>
      <linearGradient id="silver" x1="0" x2="1" y1="0" y2="0">
        <stop offset="0" stop-color="var(--silver-a)"/>
        <stop offset="0.5" stop-color="var(--silver-b)"/>
        <stop offset="1" stop-color="var(--silver-a)"/>
      </linearGradient>
    </defs>
    <path d="M0,398 C120,318 300,312 430,350 S680,440 800,365 L800,372 C700,445 560,445 420,405 S130,360 0,402 Z" fill="url(#silver)"/>
    <path d="M0,402 C130,360 290,362 420,405 S700,445 800,372 L800,457 L0,457 Z" fill="var(--leaf)"/>
  </svg>
  <div class="front-name">TIMBER RIDGE<span>LAND SERVICES</span></div>
</section>

<section class="card card-back">
  <svg class="wave" viewBox="0 0 800 457" aria-hidden="true">
    <defs>
      <linearGradient id="band" x1="0" x2="1" y1="0" y2="0">
        <stop offset="0" stop-color="var(--forest)"/>
        <stop offset="0.48" stop-color="var(--teal)"/>
        <stop offset="1" stop-color="var(--forest)"/>
      </linearGradient>
      <linearGradient id="meadow" x1="0" x2="1" y1="0" y2="0">
        <stop offset="0" stop-color="var(--leaf)"/>
        <stop offset="0.45" stop-color="var(--leaf-soft)"/>
        <stop offset="1" stop-color="var(--leaf)"/>
      </linearGradient>
    </defs>
    <path d="M0,399 C120,335 260,315 400,330 S640,430 800,367 L800,372 C690,440 560,440 430,400 S150,360 0,404 Z" fill="url(#band)"/>
    <path d="M0,404 C150,360 300,365 430,400 S690,440 800,372 L800,457 L0,457 Z" fill="url(#meadow)"/>
  </svg>

  <h1 class="back-title">TIMBER RIDGE</h1>
  <p class="back-subtitle">Land Services</p>
  <div class="website">WWW.TIMBERRIDGELAND.COM</div>

  <ul class="contact">
    <li><svg viewBox="0 0 24 24"><path d="M3 9c0-3 4-5 9-5s9 2 9 5v2h-5V9H8v2H3z M6 12h12l2 7H4z"/></svg>(850) 555 - 0147</li>
    <li><svg viewBox="0 0 24 24"><path d="M7 1h10a1 1 0 0 1 1 1v20a1 1 0 0 1-1 1H7a1 1 0 0 1-1-1V2a1 1 0 0 1 1-1zm1 3v14h8V4zm4 15.5a1.2 1.2 0 1 0 0 2.4 1.2 1.2 0 0 0 0-2.4z"/></svg>(850) 555 - 0147</li>
    <li><svg viewBox="0 0 24 24"><path d="M2 5h20v14H2z M3.5 6.5 12 13l8.5-6.5" fill="var(--forest-deep)"/><path d="M3.5 6.5 12 13l8.5-6.5" fill="none" stroke="#fff" stroke-width="1.5"/></svg>info@timberridgeland.com</li>
    <li class="address"><svg viewBox="0 0 24 24"><path d="M12 1a8 8 0 0 0-8 8c0 6 8 14 8 14s8-8 8-14a8 8 0 0 0-8-8zm0 11a3 3 0 1 1 0-6 3 3 0 0 1 0 6z"/></svg><span>4471 Pinecrest Trail Road,<br>Suite 210-B, FL 32551</span></li>
  </ul>

  <div class="back-name">TIMBER RIDGE<span>LAND SERVICES</span></div>
</section>

</body>
</html>
```